Family Ranch with a hobby vineyard needs 2 wine labels for our first harvest

Design 2 wine labels (front and back) with the Brindor Ranch logo.
Label 1:
Sauvignon Blanc
Alc. 12.5% by Vol.
Palos Verdes Peninsula - add as the region
Year 2022
Label 2:
Cabernet Sauvignon
Alc. 13.5% by Vol.
Year 2022
For the back label design:
GOVERNMENT WARNING: (1) According to the Surgeon General, women
should not drink alcoholic beverages during pregnancy because of the risk of
birth defects. (2) Consumption of alcoholic beverages impairs your ability to
drive a car or operate machinery, and may cause health problems.
Contains Sulfates.
750ML
I just received the bottles and have attached a picture.
Look and feel
Each slider illustrates characteristics of the customer's brand and the style your logo design should communicate.

```html
<!DOCTYPE html>
<html lang="en">
<head>
<meta charset="utf-8">
<title>Brindor Ranch – Sauvignon Blanc Labels</title>
<link href="https://fonts.googleapis.com/css2?family=Montserrat:wght@400;500;600&family=Overpass:wght@400;700&display=swap" rel="stylesheet">
<style>
  :root {
    --page: #ffffff;
    --label: #ffffff;
    --ink: #111111;
    --ink-soft: #1c1c1c;
    --shadow: rgba(0, 0, 0, 0.07);
  }
  html, body {
    margin: 0;
    padding: 0;
    width: 1200px;
    height: 1200px;
    overflow: hidden;
    background: var(--page);
  }
  .canvas {
    position: relative;
    width: 1200px;
    height: 1200px;
    background: var(--page);
    color: var(--ink);
  }
  .label {
    position: absolute;
    background: var(--label);
    box-shadow: 0 0 14px var(--shadow);
  }

  /* Front label */
  .label--front {
    left: 160px;
    top: 364px;
    width: 420px;
    height: 480px;
    font-family: "Montserrat", sans-serif;
    text-align: center;
  }
  .brand-mark {
    position: absolute;
    left: 50%;
    top: 102px;
    width: 86px;
    height: 86px;
    margin-left: -43px;
    border-radius: 50%;
    background: var(--ink);
  }
  .front-brand {
    position: absolute;
    left: 0;
    right: 0;
    top: 222px;
    font-weight: 600;
    font-size: 34px;
    letter-spacing: 1px;
    text-transform: uppercase;
    color: var(--ink);
    line-height: 1;
  }
  .varietal {
    position: absolute;
    left: 0;
    right: 0;
    top: 352px;
    font-weight: 400;
    font-size: 25px;
    letter-spacing: 0.5px;
    line-height: 1;
  }
  .region {
    position: absolute;
    left: 0;
    right: 0;
    top: 410px;
    font-weight: 400;
    font-size: 13.5px;
    letter-spacing: 1px;
    line-height: 1;
  }
  .vintage {
    position: absolute;
    left: 0;
    right: 0;
    top: 428px;
    font-weight: 400;
    font-size: 12px;
    letter-spacing: 1px;
    line-height: 1;
  }

  /* Back label */
  .label--back {
    left: 628px;
    top: 611px;
    width: 420px;
    height: 233px;
    font-family: "Overpass", sans-serif;
  }
  .back-brand {
    position: absolute;
    left: 31px;
    top: 64px;
    font-family: "Montserrat", sans-serif;
    font-weight: 600;
    font-size: 20px;
    letter-spacing: 0.5px;
    text-transform: uppercase;
    line-height: 1;
    color: var(--ink-soft);
  }
  .volume {
    position: absolute;
    right: 32px;
    top: 57px;
    font-weight: 700;
    font-size: 13px;
    letter-spacing: 1px;
    line-height: 1;
  }
  .abv {
    position: absolute;
    right: 32px;
    top: 101px;
    font-weight: 700;
    font-size: 14px;
    letter-spacing: 0.3px;
    line-height: 1;
  }
  .warning {
    position: absolute;
    left: 32px;
    right: 31px;
    top: 136px;
    margin: 0;
    font-weight: 400;
    font-size: 11px;
    line-height: 14.6px;
    letter-spacing: 0.2px;
    color: var(--ink-soft);
  }
  .warning strong {
    font-weight: 700;
  }
  .sulfates {
    position: absolute;
    right: 32px;
    top: 202px;
    font-weight: 700;
    font-size: 11px;
    letter-spacing: 0.2px;
    line-height: 14.6px;
  }
</style>
</head>
<body>
<main class="canvas">

  <section class="label label--front" aria-label="Front label">
    <div class="brand-mark" aria-hidden="true"></div>
    <div class="front-brand">Brindor Ranch</div>
    <div class="varietal">SAUVIGNON BLANC</div>
    <div class="region">Palos Verdes Peninsula</div>
    <div class="vintage">2023</div>
  </section>

  <section class="label label--back" aria-label="Back label">
    <div class="back-brand">Brindor Ranch</div>
    <div class="volume">750 ML</div>
    <div class="abv">Alc. 12.5% by Vol.</div>
    <p class="warning"><strong>GOVERNMENT WARNING:</strong> (1) According to the Surgeon General, women should not drink alcoholic beverages during pregnancy because of the risk of birth defects. (2) Consumption of alcoholic beverages impairs your ability to drive a car or operate machinery, and may cause health problems.</p>
    <div class="sulfates">CONTAINS SULFATES</div>
  </section>

</main>
</body>
</html>
```